Business Card Design Project

We consult with hotels on setting rates and maximizing a revenue strategy

Industry/Entity Type

Business

Contact Information for Business Card

I am not sure what I want. Our company offers high level consulting to hotels around the country but we are also laid back. I would like something that is professional but also shows the laid back side

```html
<!DOCTYPE html>
<html lang="en">
<head>
<meta charset="utf-8">
<title>Harborview Business Card</title>
<link href="https://fonts.googleapis.com/css2?family=Poiret+One&family=Saira+Semi+Condensed:wght@500&display=swap" rel="stylesheet">
<style>
  :root {
    --page: #e9e6e2;
    --teal-dark: #157570;
    --teal-mid: #2f837d;
    --teal-light: #71a6a2;
    --ink: #2b1e18;
    --white: #ffffff;
  }
  * { margin: 0; padding: 0; box-sizing: border-box; }
  html, body { width: 1200px; height: 1080px; overflow: hidden; background: var(--page); }
  .canvas { position: relative; width: 1200px; height: 1080px; }

  .card { position: absolute; width: 602px; height: 344px; box-shadow: 0 6px 14px rgba(0,0,0,.28); }

  /* Front */
  .card-front {
    left: 140px; top: 175px;
    background: linear-gradient(90deg, var(--teal-dark) 0%, var(--teal-light) 55%, var(--teal-light) 100%);
  }
  .card-front .inner {
    position: absolute; left: 22px; top: 17px; width: 558px; height: 309px;
    background: var(--white);
  }
  .wordmark {
    position: absolute; display: flex; align-items: center; gap: 12px;
    font-family: "Saira Semi Condensed", "Arial Narrow", sans-serif; font-weight: 500;
    color: var(--ink); letter-spacing: .5px; white-space: nowrap;
  }
  .wordmark .mark { background: var(--ink); flex: none; }
  .card-front .wordmark { left: 138px; top: 152px; font-size: 34px; }
  .card-front .wordmark .mark { width: 24px; height: 24px; }

  /* Back */
  .card-back { left: 420px; top: 548px; display: flex; }
  .card-back .logo-side { position: relative; width: 264px; height: 100%; background: var(--white); }
  .card-back .logo-side .wordmark { left: 40px; top: 160px; font-size: 21px; gap: 8px; }
  .card-back .logo-side .wordmark .mark { width: 15px; height: 15px; }

  .card-back .info-side {
    position: relative; flex: 1; height: 100%;
    background: linear-gradient(90deg, var(--teal-light) 0%, var(--teal-mid) 70%, var(--teal-dark) 100%);
    color: var(--white); font-family: "Poiret One", sans-serif;
  }
  .company-name { position: absolute; left: 36px; top: 24px; font-size: 43px; line-height: 1; letter-spacing: 1px; transform: scaleX(.74); transform-origin: left; white-space: nowrap; }
  .company-legal { position: absolute; left: 36px; top: 72px; font-size: 17px; white-space: nowrap; }

  .contact-row { position: absolute; left: 28px; display: flex; align-items: center; gap: 10px; font-size: 17px; white-space: nowrap; }
  .contact-row svg { width: 20px; height: 20px; fill: var(--white); flex: none; }
  .person { top: 132px; align-items: flex-start; }
  .person .name { font-size: 20px; line-height: 1.1; }
  .person .role { font-size: 14px; }
  .phone { top: 207px; }
  .fax { top: 238px; }
  .email { top: 267px; font-size: 16px; }
  .web { top: 294px; font-size: 16px; }
</style>
</head>
<body>
<div class="canvas">

  <section class="card card-front">
    <div class="inner">
      <div class="wordmark"><span class="mark"></span>HARBORVIEW</div>
    </div>
  </section>

  <section class="card card-back">
    <div class="logo-side">
      <div class="wordmark"><span class="mark"></span>HARBORVIEW</div>
    </div>
    <div class="info-side">
      <div class="company-name">HARBORVIEW</div>
      <div class="company-legal">Hotel Rate Strategy Partners LLC</div>

      <div class="contact-row person">
        <svg viewBox="0 0 20 20"><circle cx="10" cy="6" r="4.5"/><path d="M1 19c0-5 4-8 9-8s9 3 9 8z"/></svg>
        <div><div class="name">Dana Mercer</div><div class="role">Regional Revenue Manager</div></div>
      </div>

      <div class="contact-row phone">
        <svg viewBox="0 0 20 20"><path d="M5 1l3 1 1 4-2 2c1 3 3 5 6 6l2-2 4 1 1 3-2 3C9 19 1 11 2 3z"/></svg>
        <span>555-014-2200</span>
      </div>
      <div class="contact-row fax">
        <svg viewBox="0 0 20 20"><rect x="5" y="1" width="10" height="6"/><rect x="1" y="7" width="18" height="8" rx="1"/><rect x="5" y="13" width="10" height="6" fill="#6fa39f"/><rect x="6" y="14" width="8" height="4"/></svg>
        <span>555-014-3311</span>
      </div>
      <div class="contact-row email">
        <svg viewBox="0 0 20 20"><path d="M1 4h18v12H1z M2 5l8 6 8-6" stroke="#5f9c97" stroke-width="1.2"/></svg>
        <span>Dana@HarborviewRates.com</span>
      </div>
      <div class="contact-row web">
        <svg viewBox="0 0 20 20" fill="none" stroke="#fff" stroke-width="1.2" style="fill:none"><circle cx="10" cy="10" r="8.5"/><ellipse cx="10" cy="10" rx="4" ry="8.5"/><path d="M1.5 10h17M3 5.5h14M3 14.5h14"/></svg>
        <span>www.HarborviewRates.com</span>
      </div>
    </div>
  </section>

</div>
</body>
</html>
```